Business Card for a mobile physiotherapy company

I need a layout for a business card for a mobile physiotherapy company.
Slogan is "Mobile Physiotherapy - Your Road To Recovery"
Phone number is 867-402-5913
Email VantrePhysio@mailbright.ca (subject to change with website)
Website www.VantrePhysio.ca
My name and credentials: Kent Vantre Kent Vantre, BSc(kin), MPT, CAFCI, IMS
Information maybe included: Direct Billing, Services including Physiotherapy, IMS, acupuncture
Maybe include facebook and instagram logos
One side with the logo clean and sharp
Other side with details, try not to look too busy, keep everything concise

```html
<!DOCTYPE html>
<html lang="en">
<head>
<meta charset="utf-8">
<title>Vantre Physio – Business Card</title>
<link rel="stylesheet" href="https://fonts.googleapis.com/css2?family=Lato:wght@400;700&family=Roboto:wght@400&display=swap">
<style>
  :root {
    --page-bg: #1f1f1f;
    --card-bg: #222222;
    --card-edge: #2c2c2c;
    --brand-blue: #3d5f93;
    --ink-white: #f2f2f2;
    --icon-grey: #8a96a8;
  }
  * { box-sizing: border-box; margin: 0; padding: 0; }
  html, body {
    width: 1200px;
    height: 900px;
    overflow: hidden;
    background: var(--page-bg);
  }
  .canvas {
    position: relative;
    width: 1200px;
    height: 900px;
  }
  .card {
    position: absolute;
    left: 290px;
    width: 620px;
    height: 354px;
    background: linear-gradient(135deg, var(--card-bg) 0%, #272727 60%, #1e1e1e 100%);
    border: 1px solid var(--card-edge);
    box-shadow: 0 16px 40px rgba(0,0,0,0.55);
  }
  .card--front { top: 70px; }
  .card--back { top: 476px; }

  /* Front side */
  .brand {
    position: absolute;
    inset: 0;
    display: flex;
    align-items: center;
    justify-content: center;
    gap: 14px;
  }
  .brand__mark {
    width: 22px;
    height: 22px;
    background: var(--brand-blue);
  }
  .brand__name {
    font-family: "Lato", sans-serif;
    font-weight: 700;
    font-size: 40px;
    letter-spacing: 3px;
    color: var(--ink-white);
    text-transform: uppercase;
  }

  /* Back side */
  .details {
    position: absolute;
    inset: 0;
    display: flex;
    align-items: center;
    justify-content: center;
  }
  .details__person {
    text-align: right;
    padding-right: 26px;
  }
  .person__name {
    font-family: "Roboto", sans-serif;
    font-weight: 400;
    font-size: 24px;
    line-height: 1.2;
    color: var(--brand-blue);
  }
  .person__services {
    margin-top: 6px;
    font-family: "Lato", sans-serif;
    font-size: 14.5px;
    line-height: 1.45;
    color: var(--ink-white);
  }
  .details__divider {
    width: 2px;
    height: 110px;
    background: var(--ink-white);
  }
  .details__contact {
    list-style: none;
    padding-left: 26px;
  }
  .contact__item {
    display: flex;
    align-items: center;
    gap: 12px;
    font-family: "Lato", sans-serif;
    font-size: 14.5px;
    line-height: 1.75;
    color: var(--ink-white);
  }
  .contact__icon {
    width: 11px;
    height: 11px;
    flex: none;
  }
</style>
</head>
<body>
<main class="canvas">

  <section class="card card--front" aria-label="Card front">
    <div class="brand">
      <span class="brand__mark"></span>
      <span class="brand__name">Vantre Physio</span>
    </div>
  </section>

  <section class="card card--back" aria-label="Card back">
    <div class="details">
      <div class="details__person">
        <p class="person__name">Kent Vantre, BSc(kin),<br>MPT, CAFCI, IMS</p>
        <p class="person__services">Direct Billing, Services including<br>Physiotherapy, IMS, acupuncture</p>
      </div>
      <div class="details__divider"></div>
      <ul class="details__contact">
        <li class="contact__item">
          <svg class="contact__icon" viewBox="0 0 12 12" aria-hidden="true">
            <path d="M2.5 1 L4.5 1 L5.2 3.5 L4 4.5 Q5 7 7.5 8 L8.5 6.8 L11 7.5 L11 9.5 Q11 11 9.5 11 Q1 10 1 2.5 Q1 1 2.5 1 Z" fill="var(--icon-grey)"/>
          </svg>
          <span>867-402-5913</span>
        </li>
        <li class="contact__item">
          <svg class="contact__icon" viewBox="0 0 12 12" aria-hidden="true">
            <rect x="0.8" y="2.3" width="10.4" height="7.4" fill="none" stroke="var(--icon-grey)" stroke-width="1.2"/>
            <path d="M1 2.6 L6 6.5 L11 2.6" fill="none" stroke="var(--icon-grey)" stroke-width="1.2"/>
          </svg>
          <span>VantrePhysio@mailbright.ca</span>
        </li>
        <li class="contact__item">
          <svg class="contact__icon" viewBox="0 0 12 12" aria-hidden="true">
            <circle cx="6" cy="6" r="5" fill="none" stroke="var(--icon-grey)" stroke-width="1.1"/>
            <ellipse cx="6" cy="6" rx="2.2" ry="5" fill="none" stroke="var(--icon-grey)" stroke-width="1"/>
            <path d="M1 6 H11" stroke="var(--icon-grey)" stroke-width="1"/>
          </svg>
          <span>www.VantrePhysio.ca</span>
        </li>
      </ul>
    </div>
  </section>

</main>
</body>
</html>
```